Tellwick Asset Management - Corporate Letter Head Project

Looking for a classy design based on our current logo. Please find current logo source file in files. With our color scheme.

Target Market(s)

We're an investment firm, the letterhead needs to look professional and attractive to clients.

Industry/Entity Type

Hedgefund

Colors
0054AA
0677BA
7BADD7
CADEEF
E8F1F8

Requirements
Must have
• Our logo, address, phone number, and email

```html
<!DOCTYPE html>
<html lang="en">
<head>
<meta charset="utf-8">
<title>Tellwick Asset Management – Letterhead</title>
<link rel="stylesheet" href="https://fonts.googleapis.com/css2?family=Tinos:wght@400;700&display=swap">
<style>
  :root {
    --backdrop: #8f949d;
    --paper: #ffffff;
    --navy: #1b2c5a;
    --mist: #dfe3ec;
    --ink: #1b2c5a;
  }
  * { box-sizing: border-box; margin: 0; padding: 0; }
  html, body { width: 1200px; height: 900px; overflow: hidden; }
  body {
    background: var(--backdrop);
    font-family: "Tinos", "Times New Roman", serif;
    color: var(--ink);
    position: relative;
  }
  .letterhead {
    position: absolute;
    left: 298px;
    top: 26px;
    width: 604px;
    height: 848px;
    background: var(--paper);
    box-shadow: 0 6px 24px rgba(0, 0, 0, 0.18);
  }
  .brand {
    position: absolute;
    top: 40px;
    left: 40px;
    display: flex;
    align-items: center;
    gap: 10px;
  }
  .brand-square {
    width: 34px;
    height: 34px;
    border: 2px solid var(--navy);
    flex: none;
  }
  .brand-name {
    font-weight: 400;
    color: var(--navy);
    line-height: 1.05;
    text-transform: uppercase;
  }
  .brand-name .line-main { display: block; font-size: 22px; letter-spacing: 0.5px; }
  .brand-name .line-sub { display: block; font-size: 10px; letter-spacing: 6.2px; }
  .star-map {
    position: absolute;
    right: 40px;
    bottom: 40px;
    width: 160px;
    height: 230px;
    background: linear-gradient(180deg, #eef0f5 0%, var(--mist) 100%);
    border-radius: 4px;
  }
  .footer {
    position: absolute;
    left: 40px;
    bottom: 44px;
    width: 360px;
    font-size: 11px;
    line-height: 1.35;
    color: var(--navy);
  }
  .footer-name { text-transform: uppercase; font-size: 11px; }
  .footer-address { white-space: nowrap; }
  .contact-row {
    display: flex;
    align-items: center;
    gap: 10px;
    white-space: nowrap;
  }
  .contact-item { display: inline-flex; align-items: center; gap: 4px; }
  .contact-item svg { width: 10px; height: 10px; flex: none; }
</style>
</head>
<body>
  <main class="letterhead">
    <header class="brand">
      <span class="brand-square" aria-hidden="true"></span>
      <span class="brand-name">
        <span class="line-main">Tellwick Asset</span>
        <span class="line-sub">Management</span>
      </span>
    </header>

    <div class="star-map" role="img" aria-label="Faint decorative star pattern"></div>

    <footer class="footer">
      <p class="footer-name">Tellwick Asset Management</p>
      <p class="footer-address">18, Harrow Quay, Lindmoor Street, Northvale, code 30718</p>
      <p class="contact-row">
        <span class="contact-item">
          <svg viewBox="0 0 10 10" aria-hidden="true"><rect x="0.5" y="0.5" width="9" height="9" fill="none" stroke="currentColor"/><path d="M3 2.5 L4 4 L3.5 4.6 Q4.5 6 5.6 6.5 L6.2 6 L7.5 7 L7 7.8 Q4 7.5 2.3 3.2 Z" fill="currentColor"/></svg>
          044-987 654 321
        </span>
        <span class="contact-item">
          <svg viewBox="0 0 10 10" aria-hidden="true"><rect x="0.5" y="0.5" width="9" height="9" fill="none" stroke="currentColor"/><rect x="2" y="3" width="6" height="4" fill="none" stroke="currentColor" stroke-width="0.8"/><path d="M2 3 L5 5.3 L8 3" fill="none" stroke="currentColor" stroke-width="0.8"/></svg>
          info@tellwickasset.com
        </span>
        <span class="contact-item">
          <svg viewBox="0 0 10 10" aria-hidden="true"><rect x="0.5" y="0.5" width="9" height="9" fill="none" stroke="currentColor"/><circle cx="5" cy="5" r="2.8" fill="none" stroke="currentColor" stroke-width="0.8"/><path d="M2.2 5 H7.8 M5 2.2 V7.8" stroke="currentColor" stroke-width="0.6"/></svg>
          www.tellwickasset.com
        </span>
      </p>
    </footer>
  </main>
</body>
</html>
```